Halvik Partners Building Business Cards

We need a business card that reflects our business as "Solar Experts" in San Diego. Browse our website www.halvikpartners.example our License needs to be displayed as "CSLB# 4871306" our phone number is (619) 482-5537

Save thousands on your electric bills and increase the value of your home while helping to protect the environment. Our solar installation experts will help you design the system that's right for you, using only the highest quality equipment that will look great and give you ideal performance. Our goal is to make you energy independent, and get your electric bill to 0.

Paul Ostrander
(619) 482-5537
paul@halvikpartners.example

Target Market(s)

Home owners in san diego looking for solar

Industry/Entity Type

Solar Energy

Contact Information for Business Card

Paul Ostrander
(619) 482-5537
paul@halvikpartners.example

Font styles to use
Other font styles liked:
• Use our logo font

Requirements
Must have
• License needs to be displayed as "CSLB# 4871306" our phone number is (619) 482-5537
Nice to have
• Real images of rooftop home solar in san diego
Should not have
• our business address

```html
<!DOCTYPE html>
<html lang="en">
<head>
<meta charset="utf-8">
<title>Halvik Partners Building – Business Cards</title>
<link rel="stylesheet" href="https://fonts.googleapis.com/css2?family=Open+Sans:wght@400;700&family=Oswald:wght@600&display=swap">
<style>
  :root {
    --brand-blue: #1f63b4;
    --brand-blue-dark: #174f93;
    --sun-yellow: #f5c21b;
    --paper: #fbfbfb;
    --paper-shade: #eeeeee;
    --ink-white: #ffffff;
    --stage: #e4e6ea;
    --frame-blue: #2a5ea8;
  }
  * { box-sizing: border-box; margin: 0; padding: 0; }
  html, body {
    width: 1200px; height: 1000px; overflow: hidden;
    background: var(--stage);
    font-family: "Open Sans", Arial, sans-serif;
  }
  .canvas {
    position: relative; width: 1200px; height: 1000px;
  }
  .card {
    position: absolute; left: 250px; width: 700px; height: 400px;
    background: var(--paper);
    box-shadow: 0 10px 30px rgba(0,0,0,0.18);
    overflow: hidden;
  }
  .card--front { top: 70px; display: flex; }
  .card--back { top: 530px; }

  /* Front */
  .front-brand {
    width: 48%; height: 100%;
    background: linear-gradient(180deg, var(--paper) 0%, var(--paper-shade) 100%);
    display: flex; align-items: center; justify-content: center;
  }
  .brand-name {
    color: var(--brand-blue);
    font-weight: 700;
    font-family: "Open Sans", Arial, sans-serif;
    text-align: center;
    line-height: 1.1;
    display: flex; align-items: center; gap: 12px;
  }
  .brand-name .dot {
    width: 18px; height: 18px; border-radius: 50%;
    background: var(--brand-blue); flex: none;
  }
  .front-brand .brand-name { font-size: 30px; max-width: 280px; }

  .front-contact {
    position: relative;
    width: 52%; height: 100%;
    background: linear-gradient(160deg, var(--brand-blue) 0%, var(--brand-blue-dark) 100%);
    color: var(--ink-white);
    padding: 70px 40px 0 50px;
  }
  .front-contact::before {
    content: ""; position: absolute; left: -18px; top: 78px;
    border-top: 18px solid transparent; border-bottom: 18px solid transparent;
    border-right: 18px solid var(--brand-blue);
  }
  .contact-name {
    font-family: "Oswald", "Arial Narrow", sans-serif;
    font-weight: 600; font-size: 30px; letter-spacing: 0.5px;
    text-transform: uppercase; margin-bottom: 36px;
  }
  .contact-list { list-style: none; font-size: 17px; }
  .contact-list li {
    display: flex; align-items: center; gap: 12px; margin-bottom: 12px;
  }
  .contact-list svg { width: 16px; height: 16px; flex: none; }
  .accent { color: var(--sun-yellow); }
  .contact-license { margin-top: 26px; font-size: 17px; }

  /* Back */
  .back-frame {
    position: absolute; inset: 22px;
    border: 1.5px solid var(--frame-blue);
  }
  .back-brand {
    position: absolute; inset: 0;
    display: flex; align-items: center; justify-content: center;
  }
  .back-brand .brand-name { font-size: 46px; max-width: 520px; }
  .back-brand .brand-name .dot { width: 26px; height: 26px; }
  .back-web {
    position: absolute; left: 50px; bottom: 44px;
    font-size: 15px; font-style: italic; color: var(--frame-blue);
  }
</style>
</head>
<body>
<main class="canvas">
  <section class="card card--front">
    <div class="front-brand">
      <div class="brand-name"><span class="dot"></span><span>Halvik Partners Building</span></div>
    </div>
    <div class="front-contact">
      <h1 class="contact-name">Paul Ostrander</h1>
      <ul class="contact-list">
        <li>
          <svg viewBox="0 0 16 16"><rect x="2" y="2" width="12" height="12" rx="1" fill="none" stroke="#fff" stroke-width="1.5"/></svg>
          <span>(619) 482-5537</span>
        </li>
        <li>
          <svg viewBox="0 0 16 16"><rect x="1.5" y="3.5" width="13" height="9" fill="none" stroke="#fff" stroke-width="1.3"/><path d="M1.5 3.5 L8 9 L14.5 3.5" fill="none" stroke="#fff" stroke-width="1.3"/></svg>
          <span>paul@halvikpartners.example</span>
        </li>
        <li>
          <svg viewBox="0 0 16 16"><circle cx="8" cy="8" r="6.5" fill="none" stroke="#fff" stroke-width="1.3"/><ellipse cx="8" cy="8" rx="3" ry="6.5" fill="none" stroke="#fff" stroke-width="1.1"/><path d="M1.5 8 H14.5" stroke="#fff" stroke-width="1.1"/></svg>
          <span>www.<span class="accent">halvikpartners</span>.example</span>
        </li>
      </ul>
      <p class="contact-license">License: <span class="accent">"CSLB# 4871306"</span></p>
    </div>
  </section>

  <section class="card card--back">
    <div class="back-frame"></div>
    <div class="back-brand">
      <div class="brand-name"><span class="dot"></span><span>Halvik Partners Building</span></div>
    </div>
    <p class="back-web">www.halvikpartners.example</p>
  </section>
</main>
</body>
</html>
```